Modern and strong website design for a Dutch crowdsourcing company
.

We are startup company providing crowdsourcing of administrative and customers service tasks for larger companies and other organizations. We offer cost savings and scale-ability combined with higher quality of execution. We will soon enter the market and need a website that has two major target groups: 1. Our corporate customers 2. The mainly younger crowd executing the tasks on our platform.
The target group of customers are Influencers and decision makers with companies and other organizations in with large administrative and customer service departments. Most information in the startup phase will be targeting this group.
The target group of future crowd workers will be heterogeneous, from students to stay at home mums or night shift workers who want to earn some extra money by performing easy to execute microtasks in the cloud. We will target both Dutch and international workers.

The website must be developed for browsing on a computer but also be optimized for mobile devices and tablets.
The website must be optimized and tested for the major browsers on windows, macOS and mobile devices.

For the minimum requirement for the website see attached wireframes

The present landing page http://bravolinkhive.com and logo are not reflecting our preferences!
See enclosed a new logo that stands for both the crowdwork (performed for our customers) and the crowd (a hive in motion).

Target Market(s)

see tekst above.

Industry/Entity Type

Business Service

Coding

Coded - Design and coding required

Number of Pages Required

5+ page

Font styles to use
Sans Serif
Other font styles liked:
• Lato, Open Sans

Colors

Designer to choose colors to be used in the design.

Requirements
Must have
• start devider screen
• home page displaying business and worker information
• a page displaying only info for businesses
• a page displaying only info for workers
• a contact form
• a reviews page
• color scheme from logo
• responsiveness!
Nice to have
• Nice animations
• overlapping blocks, animated on scroll
• lightbox effects if applicable
• animated mobile menu icon and menu itself

```html
<!DOCTYPE html>
<html lang="en">
<head>
<meta charset="utf-8">
<title>A Hive in Motion — Choose your path</title>
<link rel="stylesheet" href="https://fonts.googleapis.com/css2?family=Cabin:wght@500;600&display=swap">
<style>
  :root {
    --orange: #e8650f;
    --orange-deep: #d45a0a;
    --grey-dark: #555556;
    --grey-mid: #727273;
    --grey-text: #6b6b6c;
    --ink: #1e1e1e;
    --panel-top: rgba(246, 245, 243, 0.90);
    --panel-bottom: rgba(236, 235, 232, 0.80);
    --white: #ffffff;
  }
  * { box-sizing: border-box; margin: 0; padding: 0; }
  html, body {
    width: 1200px;
    height: 583px;
    overflow: hidden;
  }
  body {
    position: relative;
    font-family: "Cabin", sans-serif;
    background: #262522;
  }
  .city-backdrop {
    position: absolute;
    inset: 0;
    background:
      radial-gradient(ellipse 420px 160px at 640px 70px, rgba(190, 186, 176, 0.45), transparent 70%),
      radial-gradient(ellipse 700px 120px at 600px 330px, rgba(120, 116, 106, 0.35), transparent 75%),
      linear-gradient(180deg,
        #252320 0%,
        #3d3931 14%,
        #5a554a 28%,
        #4a4840 38%,
        #38373a 48%,
        #2c2b29 58%,
        #3c3b37 68%,
        #35342f 78%,
        #201f1d 90%,
        #1a1918 100%);
  }
  .gateway-panel {
    position: absolute;
    left: 315px;
    top: 69px;
    width: 570px;
    height: 445px;
    border-radius: 10px;
    background: linear-gradient(180deg, var(--panel-top), var(--panel-bottom));
    box-shadow: 0 10px 40px rgba(0, 0, 0, 0.25);
    display: flex;
    flex-direction: column;
    align-items: center;
  }
  .brand {
    margin-top: 45px;
    display: flex;
    flex-direction: column;
    align-items: center;
  }
  .brand-dot {
    width: 134px;
    height: 134px;
    border-radius: 50%;
    background: var(--orange);
  }
  .brand-name {
    margin-top: 30px;
    font-size: 36px;
    font-weight: 600;
    line-height: 1;
    color: var(--grey-text);
  }
  .for-label {
    margin-top: 56px;
    font-size: 20px;
    font-weight: 600;
    letter-spacing: 0.5px;
    color: var(--ink);
  }
  .audience-choice {
    margin-top: 25px;
    display: flex;
    gap: 19px;
  }
  .audience-button {
    height: 49px;
    border-radius: 25px;
    display: flex;
    align-items: center;
    justify-content: center;
    gap: 9px;
    color: var(--white);
    font-size: 20px;
    font-weight: 500;
    letter-spacing: 0.3px;
    text-decoration: none;
  }
  .audience-button svg { fill: var(--white); }
  .audience-button--workers {
    width: 201px;
    background: linear-gradient(90deg, var(--grey-dark), var(--grey-mid));
  }
  .audience-button--businesses {
    width: 207px;
    background: linear-gradient(90deg, var(--orange-deep), var(--orange));
  }
</style>
</head>
<body>
  <div class="city-backdrop" role="img" aria-label="Photograph of a waterfront city skyline with high-rise towers under dark storm clouds"></div>

  <main class="gateway-panel">
    <div class="brand">
      <span class="brand-dot" aria-hidden="true"></span>
      <span class="brand-name">A Hive in Motion</span>
    </div>

    <p class="for-label">FOR</p>

    <nav class="audience-choice">
      <a class="audience-button audience-button--workers" href="#workers">
        <svg width="22" height="18" viewBox="0 0 22 18" aria-hidden="true">
          <circle cx="4.5" cy="4" r="2.6"/>
          <circle cx="17.5" cy="4" r="2.6"/>
          <circle cx="11" cy="4.5" r="3.4"/>
          <path d="M0 12c0-3 2-4.5 4.5-4.5S9 9 9 12v1H0z"/>
          <path d="M13 12c0-3 2-4.5 4.5-4.5S22 9 22 12v1h-9z"/>
          <path d="M5.5 17c0-4 2.3-6.5 5.5-6.5s5.5 2.5 5.5 6.5v1h-11z"/>
        </svg>
        WORKERS
      </a>
      <a class="audience-button audience-button--businesses" href="#businesses">
        <svg width="12" height="24" viewBox="0 0 12 24" aria-hidden="true">
          <circle cx="6" cy="3" r="3"/>
          <path d="M1.5 7h9c.8 0 1.5.7 1.5 1.5V15h-2v9H7.2v-7H4.8v7H2v-9H0V8.5C0 7.7.7 7 1.5 7z"/>
        </svg>
        BUSINESSES
      </a>
    </nav>
  </main>
</body>
</html>
```